lantern institute of business and technology web site

I need web site for the institute which focus on business courses and computer course it is also for vocation train for employment It is also carear development and advancement .It should have links to online study resource which free
Industry/Entity Type
Business
Number of Pages Required
1 page
Look and feel

```html
<!DOCTYPE html>
<html lang="en">
<head>
<meta charset="utf-8">
<title>Lantern Institute of Business and Technology</title>
<link href="https://fonts.googleapis.com/css2?family=Open+Sans:wght@400;600;700&display=swap" rel="stylesheet">
<style>
:root{
  --blue:#1e7fd0;
  --blue-dark:#1567ad;
  --ink:#333a40;
  --muted:#6d737a;
  --light:#ececec;
  --white:#ffffff;
  --footer:#3b3d40;
  --footer-box:#4a4d51;
  --topbar:#2d2f33;
}
*{box-sizing:border-box;margin:0;padding:0}
html,body{width:1200px;height:2280px;overflow:hidden}
body{font-family:"Open Sans",Arial,sans-serif;color:var(--ink);background:var(--white);font-size:13px;line-height:1.55}
.wrap{width:880px;margin:0 auto;position:relative}

/* Header */
.site-header{background:var(--blue);height:580px;position:relative}
.top-links{position:absolute;left:0;top:0;background:var(--topbar);color:var(--white);font-size:11px;font-weight:600;letter-spacing:.5px;padding:12px 22px;border-radius:0 0 6px 6px}
.socials{position:absolute;right:0;top:20px;display:flex;gap:10px}
.socials span{width:26px;height:26px;border-radius:50%;background:var(--blue-dark);border:1px solid rgba(255,255,255,.35)}
.brand{position:absolute;left:0;top:84px;color:var(--white)}
.brand-name{font-size:26px;font-weight:700;letter-spacing:1px;line-height:1}
.brand-tag{font-size:10px;opacity:.85;margin-top:4px}
.main-nav{position:absolute;right:0;top:92px;display:flex;gap:4px}
.main-nav a{color:var(--white);text-decoration:none;font-size:12px;padding:12px 16px}
.main-nav a.active{background:var(--white);color:var(--blue);padding-top:20px;margin-top:-8px}
.hero{position:absolute;left:0;top:152px;width:632px;height:392px;background:linear-gradient(135deg,#b9b2a6,#6f6a66 55%,#2d2a2a)}
.slider-dots{position:absolute;left:18px;bottom:16px;display:flex;gap:6px}
.slider-dots span{width:20px;height:20px;background:rgba(20,20,20,.7);color:#fff;font-size:10px;text-align:center;line-height:20px}
.slider-dots span.on{background:var(--blue)}
.side{position:absolute;right:0;top:152px;width:232px}
.video{height:200px;background:linear-gradient(135deg,#1b3d8f,#0d1f52);position:relative}
.video .play{position:absolute;left:50%;top:50%;width:44px;height:44px;margin:-22px 0 0 -22px}
.side-text{color:var(--white);font-size:11px;line-height:1.45;margin-top:10px}
.join{margin-top:34px;height:92px;display:flex;background:var(--white)}
.join .thumb{width:92px;background:linear-gradient(135deg,#c7cdd4,#7c8794)}
.join .label{flex:1;display:flex;align-items:center;justify-content:center;font-size:20px;font-weight:600;color:var(--blue);line-height:1.1;text-align:left}

/* Intro */
.intro{height:430px;padding-top:30px;text-align:center}
.section-title{font-size:24px;font-weight:600;color:var(--ink)}
.section-sub{font-size:15px;color:var(--muted);margin-top:2px}
.intro p{font-size:11px;color:var(--muted);margin:20px auto 0;width:800px}
.cards{display:flex;gap:24px;margin-top:40px;text-align:left}
.card{flex:1}
.card .pic{height:104px}
.card h4{color:var(--blue);font-size:13px;font-weight:600;margin-top:10px}
.card p{width:auto;margin:6px 0 0;font-size:10.5px;color:var(--muted)}

/* Features */
.features{background:var(--light);height:400px;padding-top:66px}
.features .section-title{text-align:center;font-size:18px}
.feature-grid{display:grid;grid-template-columns:1fr 1fr;gap:36px 60px;margin-top:36px}
.feature{display:flex;gap:18px}
.num{flex:none;width:56px;height:56px;border-radius:50%;background:var(--white);border:1px solid #d6d6d6;display:flex;align-items:center;justify-content:center;font-size:18px;font-weight:600;color:var(--ink)}
.num.on{background:var(--blue);color:var(--white);border-color:var(--blue)}
.feature h4{color:var(--blue);font-size:12px;font-weight:600}
.feature p{font-size:10.5px;color:var(--muted);line-height:1.5}
.feature .more{font-size:10px;color:var(--ink);margin-top:4px}

/* Services */
.services{height:170px;padding-top:54px;border-bottom:1px solid #e2e2e2}
.service-row{display:flex;gap:36px}
.service{flex:1;display:flex;gap:14px}
.icon{flex:none;width:42px;height:42px;border-radius:50%;border:2px solid var(--blue);display:flex;align-items:center;justify-content:center}
.service h4{color:var(--blue);font-size:13px;font-weight:600}
.service p{font-size:10.5px;color:var(--muted);line-height:1.45}

/* Gallery */
.gallery{height:400px;padding-top:46px}
.ruled-title{display:flex;align-items:center;gap:20px;justify-content:center}
.ruled-title::before,.ruled-title::after{content:"";width:220px;height:1px;background:#d4d4d4}
.ruled-title h3{font-size:18px;font-weight:600}
.gallery-row{display:flex;gap:20px;margin-top:28px}
.gallery-item{flex:1}
.gallery-item .pic{height:188px}
.gallery-item p{font-size:11px;color:var(--muted);margin-top:12px}

/* Footer */
.site-footer{background:var(--footer);height:300px;color:#d9dadb;padding-top:46px;position:relative}
.footer-cols{display:flex;gap:40px}
.footer-col{flex:1;font-size:10.5px;line-height:1.6}
.footer-col h5{color:var(--white);font-size:13px;font-weight:600;margin-bottom:10px}
.footer-col.why{background:var(--footer-box);padding:18px 22px;margin-top:-18px;flex:1.2}
.footer-col.why h5{letter-spacing:2px;font-size:11px}
.footer-col.why li{list-style:none;padding-left:14px;position:relative;margin-bottom:6px}
.footer-col.why li::before{content:"";position:absolute;left:0;top:6px;width:5px;height:5px;border-radius:50%;background:var(--blue)}
.copyright{position:absolute;left:0;right:0;bottom:14px;text-align:center;font-size:9.5px;color:#9a9c9f;border-top:1px solid #55585c;padding-top:10px;width:880px;margin:0 auto}
</style>
</head>
<body>

<header class="site-header">
  <div class="wrap">
    <div class="top-links">COURSES | STUDENT LOGIN | STAFF LOGIN | CONTACT</div>
    <div class="socials"><span></span><span></span><span></span><span></span><span></span></div>
    <div class="brand">
      <div class="brand-name">LANTERN</div>
      <div class="brand-tag">Institute of Business and Technology</div>
    </div>
    <nav class="main-nav">
      <a class="active" href="#">Home</a>
      <a href="#">About</a>
      <a href="#">Courses</a>
      <a href="#">Services</a>
      <a href="#">Gallery</a>
      <a href="#">Contact us</a>
    </nav>
    <div class="hero" role="img" aria-label="Photo of hands typing on a laptop keyboard">
      <div class="slider-dots"><span class="on">1</span><span>2</span><span>3</span><span>4</span></div>
    </div>
    <aside class="side">
      <div class="video" role="img" aria-label="Video thumbnail with online study theme">
        <svg class="play" viewBox="0 0 44 44"><circle cx="22" cy="22" r="21" fill="rgba(255,255,255,.25)" stroke="#fff" stroke-width="2"/><path d="M17 13 L32 22 L17 31 Z" fill="#fff"/></svg>
      </div>
      <p class="side-text">Lorem ipsum dolor sit amet, consectetur adipiscing elit sed do eiusmod tempor incididunt.</p>
      <div class="join">
        <div class="thumb" role="img" aria-label="Photo of a student"></div>
        <div class="label">JOIN<br>TODAY</div>
      </div>
    </aside>
  </div>
</header>

<section class="intro">
  <div class="wrap">
    <h2 class="section-title">Lorem Ipsum is simply dummy</h2>
    <div class="section-sub">type and scrambled specimen</div>
    <p>Lorem Ipsum is simply dummy text of the printing and typesetting industry. Lorem Ipsum has been the industry's standard dummy text ever since the 1500s, when an unknown printer took a galley of type and scrambled it to make a type specimen book. It has survived not only five centuries, but also the leap into electronic typesetting, remaining essentially unchanged.</p>
    <div class="cards">
      <div class="card">
        <div class="pic" role="img" aria-label="Photo of students at a computer" style="background:linear-gradient(135deg,#c9d6e3,#6d8aa6)"></div>
        <h4>Lorem Ipsum is simply</h4>
        <p>Lorem ipsum is simply dummy text of the printing and typesetting industry standard text.</p>
      </div>
      <div class="card">
        <div class="pic" role="img" aria-label="Photo of a classroom lesson" style="background:linear-gradient(135deg,#e2d7c6,#9b8772)"></div>
        <h4>Lorem Ipsum is simply</h4>
        <p>Lorem ipsum is simply dummy text of the printing and typesetting industry standard text.</p>
      </div>
      <div class="card">
        <div class="pic" role="img" aria-label="Photo of a business meeting" style="background:linear-gradient(135deg,#d3dbe4,#7b8a9c)"></div>
        <h4>Lorem Ipsum is simply</h4>
        <p>Lorem ipsum is simply dummy text of the printing and typesetting industry standard text.</p>
      </div>
      <div class="card">
        <div class="pic" role="img" aria-label="Photo of a student studying" style="background:linear-gradient(135deg,#d8d2cc,#8a7f79)"></div>
        <h4>Lorem Ipsum is simply</h4>
        <p>Lorem ipsum is simply dummy text of the printing and typesetting industry standard text.</p>
      </div>
    </div>
  </div>
</section>

<section class="features">
  <div class="wrap">
    <h2 class="section-title">Lorem Ipsum is simply dummy</h2>
    <div class="feature-grid">
      <div class="feature"><div class="num on">01</div><div><h4>Lorem Ipsum is simply</h4><p>Lorem ipsum dolor sit amet, consectetur adipiscing elit, sed do eiusmod tempor incididunt ut labore et dolore magna aliqua enim minim.</p><div class="more">See More...</div></div></div>
      <div class="feature"><div class="num">03</div><div><h4>Lorem Ipsum is simply</h4><p>Lorem ipsum dolor sit amet, consectetur adipiscing elit, sed do eiusmod tempor incididunt ut labore et dolore magna aliqua enim minim.</p><div class="more">See More...</div></div></div>
      <div class="feature"><div class="num">02</div><div><h4>Lorem Ipsum is simply</h4><p>Lorem ipsum dolor sit amet, consectetur adipiscing elit, sed do eiusmod tempor incididunt ut labore et dolore magna aliqua enim minim.</p><div class="more">See More...</div></div></div>
      <div class="feature"><div class="num">04</div><div><h4>Lorem Ipsum is simply</h4><p>Lorem ipsum dolor sit amet, consectetur adipiscing elit, sed do eiusmod tempor incididunt ut labore et dolore magna aliqua enim minim.</p><div class="more">See More...</div></div></div>
    </div>
  </div>
</section>

<section class="services">
  <div class="wrap service-row">
    <div class="service">
      <div class="icon"><svg width="22" height="22" viewBox="0 0 22 22"><rect x="3" y="4" width="16" height="11" rx="1" fill="none" stroke="#1e7fd0" stroke-width="2"/><path d="M1 18 H21" stroke="#1e7fd0" stroke-width="2"/></svg></div>
      <div><h4>Lorem Ipsum is simply dummy</h4><p>Lorem Ipsum is simply dummy text of the printing and typesetting industry. Lorem Ipsum.</p></div>
    </div>
    <div class="service">
      <div class="icon"><svg width="22" height="22" viewBox="0 0 22 22"><path d="M2 5 H10 V18 H2 Z M12 5 H20 V18 H12 Z" fill="none" stroke="#1e7fd0" stroke-width="2"/></svg></div>
      <div><h4>Lorem Ipsum is simply dummy</h4><p>Lorem Ipsum is simply dummy text of the printing and typesetting industry. Lorem Ipsum.</p></div>
    </div>
    <div class="service">
      <div class="icon"><svg width="22" height="22" viewBox="0 0 22 22"><path d="M3 8 L11 4 L19 8 L11 12 Z" fill="#1e7fd0"/><path d="M6 10 V15 C8 17 14 17 16 15 V10" fill="none" stroke="#1e7fd0" stroke-width="2"/></svg></div>
      <div><h4>Lorem Ipsum is simply dummy</h4><p>Lorem Ipsum is simply dummy text of the printing and typesetting industry. Lorem Ipsum.</p></div>
    </div>
  </div>
</section>

<section class="gallery">
  <div class="wrap">
    <div class="ruled-title"><h3>Lorem Ipsum is simply dummy</h3></div>
    <div class="gallery-row">
      <div class="gallery-item">
        <div class="pic" role="img" aria-label="Photo of students writing in class" style="background:linear-gradient(135deg,#e6d4b8,#a98b62)"></div>
        <p>Lorem Ipsum is simply dummy text of the printing and typesetting industry.</p>
      </div>
      <div class="gallery-item">
        <div class="pic" role="img" aria-label="Photo of a lecture hall" style="background:linear-gradient(135deg,#f1f1f1,#b7b7b7)"></div>
        <p>Lorem Ipsum is simply dummy text of the printing and typesetting industry.</p>
      </div>
      <div class="gallery-item">
        <div class="pic" role="img" aria-label="Photo of graduates celebrating" style="background:linear-gradient(135deg,#c7b3c0,#7a3f4f)"></div>
        <p>Lorem Ipsum is simply dummy text of the printing and typesetting industry.</p>
      </div>
    </div>
  </div>
</section>

<footer class="site-footer">
  <div class="wrap">
    <div class="footer-cols">
      <div class="footer-col">
        <h5>About us</h5>
        <p>Lorem ipsum dolor sit amet, consectetur adipiscing elit. Sed ut perspiciatis unde omnis iste natus error sit voluptatem accusantium doloremque laudantium totam rem.</p>
        <p style="margin-top:8px">» Read More</p>
      </div>
      <div class="footer-col why">
        <h5>WHY US...</h5>
        <ul>
          <li>Lorem Ipsum is simply dummy text of the</li>
          <li>Printing and typesetting industry Lorem</li>
          <li>Has been the industry's standard dummy text</li>
          <li>Ever since the 1500s when an unknown</li>
        </ul>
      </div>
      <div class="footer-col">
        <h5>Contact Details</h5>
        <p>lanterninstitute.edu<br>Mobile<br>Lorem ipsum consectetur<br>Lorem ipsum consectetur Pvt.<br>Lorem ipsum &amp; dolor sit<br>Lantern Road 00000</p>
      </div>
    </div>
  </div>
  <div class="copyright">Copyright © 2024 Lantern. All Rights Reserved</div>
</footer>

</body>
</html>
```